Full service meeting planning company needs new business cards

Velmora Linkway is a full service meeting planning company that specializes in on-line conference registration web development and event communications. We combine citywide hotel management, mobile applications, eblast reminders, confirmation letters, and customized reporting to create a seamless registration process. We also manage group motor coach transportation, food and beverages, entertainment, stage and lighting for group of 10 to 4000.

Target Market(s)

Corporations and associations

Industry/Entity Type

Event Planning

Contact Information for Business Card

standard size 3.5" wide and 2" tall

Font styles to use
Serif
Sans Serif

Colors
f37122
f78f20
333333
5c5c5c
9d9d9d
f68d4d

Requirements
Must have
• {name}
• Velmora Linkway
• P.O. Box 7384, Grand Rapids, M I 49568
• www.velmoralinkway.com
• {email}
• {phone}
• {mobile phone}
Nice to have
• Our colors are black, grey and orange as an accent color
Should not have
• I am not happy with our website layout anymore either. It feels dark and old but it does explain who we are pretty well if you'd like to review; www.velmoralinkway.com

```html
<!DOCTYPE html>
<html lang="en">
<head>
<meta charset="utf-8">
<title>Velmora Linkway – Business Card</title>
<link rel="stylesheet" href="https://fonts.googleapis.com/css2?family=Fira+Sans:wght@300;500;800&display=swap">
<style>
  :root {
    --orange: #f37122;
    --orange-light: #f78f20;
    --white: #ffffff;
    --ink: #333333;
    --backdrop: #e9e6e2;
    --shadow: rgba(51, 51, 51, 0.18);
  }
  * { margin: 0; padding: 0; box-sizing: border-box; }
  html, body {
    width: 1200px;
    height: 1033px;
    overflow: hidden;
    background: var(--backdrop);
    font-family: "Fira Sans", sans-serif;
  }
  .sheet {
    width: 1200px;
    height: 1033px;
    display: flex;
    flex-direction: column;
    align-items: center;
    justify-content: center;
    gap: 80px;
  }
  .card {
    position: relative;
    width: 700px;
    height: 400px;
    box-shadow: 0 10px 30px var(--shadow);
  }
  .card-front {
    background: var(--orange);
    color: var(--white);
  }
  .mailing-block {
    position: absolute;
    left: 44px;
    top: 92px;
    font-weight: 300;
    font-size: 15px;
    line-height: 1.35;
  }
  .identity {
    position: absolute;
    left: 0;
    right: 0;
    top: 150px;
    text-align: center;
  }
  .person-name {
    font-weight: 800;
    font-size: 36px;
    letter-spacing: 0.5px;
  }
  .company-name {
    font-weight: 300;
    font-size: 16px;
    margin-top: 4px;
  }
  .direct-block {
    position: absolute;
    right: 44px;
    top: 110px;
    text-align: right;
    font-weight: 300;
    font-size: 15px;
    line-height: 1.35;
  }
  .card-back {
    background: var(--white);
    display: flex;
    align-items: center;
    justify-content: center;
    gap: 14px;
  }
  .brand-dot {
    width: 22px;
    height: 22px;
    border-radius: 50%;
    border: 2px solid var(--orange);
  }
  .brand-name {
    color: var(--orange);
    font-weight: 500;
    font-size: 30px;
  }
</style>
</head>
<body>
  <main class="sheet">
    <section class="card card-front" aria-label="Business card front">
      <address class="mailing-block" style="font-style: normal;">
        P.O. Box 7384<br>
        Grand Rapids, MI 49568<br>
        616 555 0143<br>
        velmoralinkway.com
      </address>
      <div class="identity">
        <h1 class="person-name">Marisa Koenig</h1>
        <p class="company-name">Velmora Linkway</p>
      </div>
      <address class="direct-block" style="font-style: normal;">
        mkoenig@velmoralinkway.com<br>
        616 555 0143 x09
      </address>
    </section>
    <section class="card card-back" aria-label="Business card back">
      <span class="brand-dot" aria-hidden="true"></span>
      <span class="brand-name">Velmora Linkway</span>
    </section>
  </main>
</body>
</html>
```